KORBALT

The business want a professional looking business card. We have a scetch we will add but want the extra upgrade, and would like more suggestions for variations of our business cards.

```html
<!DOCTYPE html>
<html lang="en">
<head>
<meta charset="UTF-8">
<title>KORBALT Business Card</title>
<link href="https://fonts.googleapis.com/css2?family=Playfair+Display:wght@700&family=Montserrat:wght@400;500&display=swap" rel="stylesheet">
<style>
  :root {
    --page-bg: #3a3a3c;
    --card-black: #141414;
    --card-edge: #0c0c0c;
    --gold-light: #f3d27a;
    --gold: #d4a43a;
    --gold-dark: #9a6f1c;
    --text-light: #e8e8e8;
    --pattern-silver: #9a9a9a;
  }
  * { margin: 0; padding: 0; box-sizing: border-box; }
  html, body { width: 1200px; height: 875px; overflow: hidden; }
  body {
    background: var(--page-bg);
    display: flex;
    flex-direction: column;
    align-items: center;
    justify-content: center;
    gap: 44px;
  }
  .card {
    width: 660px;
    height: 378px;
    border-radius: 22px;
    background: var(--card-black);
    position: relative;
    overflow: hidden;
    border-bottom: 3px solid var(--gold);
    border-left: 2px solid var(--gold-dark);
  }
  .card-back .pattern-field {
    position: absolute;
    inset: 0;
    background: linear-gradient(120deg, #8a8a8a 0%, #4a4a4a 28%, #1e1e1e 55%, var(--card-edge) 100%);
  }
  .card-front {
    display: flex;
    align-items: center;
    padding: 0 56px 0 60px;
  }
  .brand {
    width: 230px;
    text-align: center;
  }
  .brand-mark {
    width: 18px; height: 18px;
    border-radius: 50%;
    background: var(--gold);
    margin: 0 auto 18px;
  }
  .brand-name {
    font-family: "Playfair Display", serif;
    font-weight: 700;
    font-size: 44px;
    letter-spacing: 2px;
    color: var(--gold);
    line-height: 1;
  }
  .brand-since {
    font-family: "Montserrat", sans-serif;
    font-size: 11px;
    letter-spacing: 6px;
    color: var(--gold);
    margin-top: 10px;
  }
  .divider {
    width: 1.5px;
    height: 170px;
    background: linear-gradient(var(--gold-light), var(--gold-dark));
    margin: 0 34px 0 28px;
  }
  .contact { flex: 1; }
  .person-name {
    font-family: "Playfair Display", serif;
    font-weight: 700;
    font-size: 31px;
    color: var(--gold-light);
    line-height: 1.1;
  }
  .person-title {
    font-family: "Montserrat", sans-serif;
    font-size: 15px;
    color: var(--text-light);
    margin: 6px 0 20px;
  }
  .contact-list { list-style: none; }
  .contact-list li {
    display: flex;
    align-items: center;
    gap: 10px;
    font-family: "Montserrat", sans-serif;
    font-size: 15px;
    color: var(--text-light);
    line-height: 1.75;
  }
  .contact-list svg { width: 13px; height: 13px; fill: var(--gold); flex: none; }
</style>
</head>
<body>
  <section class="card card-back">
    <div class="pattern-field" role="img" aria-label="Repeating floral brand pattern fading from silver gloss to black on black"></div>
  </section>

  <section class="card card-front">
    <div class="brand">
      <div class="brand-mark"></div>
      <div class="brand-name">KORBALT</div>
      <div class="brand-since">SINCE 2026</div>
    </div>
    <div class="divider"></div>
    <div class="contact">
      <h1 class="person-name">Lars Henrik Dalvang</h1>
      <p class="person-title">CEO &amp; Founder</p>
      <ul class="contact-list">
        <li><svg viewBox="0 0 16 16"><path d="M3 1h3l1 4-2 1c1 2 3 4 5 5l1-2 4 1v3c0 1-1 2-2 2C7 15 1 9 1 3c0-1 1-2 2-2z"/></svg>004791234567</li>
        <li><svg viewBox="0 0 16 16"><path d="M1 3h14v10H1z M2 4l6 5 6-5" stroke="#141414" stroke-width="1.2"/></svg>korbalt.llc@postmail.com</li>
        <li><svg viewBox="0 0 16 16"><circle cx="8" cy="8" r="7"/><path d="M1 8h14M8 1c-3 4-3 10 0 14M8 1c3 4 3 10 0 14" stroke="#141414" stroke-width="1" fill="none"/></svg>www.korbalt.llc</li>
      </ul>
    </div>
  </section>
</body>
</html>
```